Tallowfern Studio business cards

We are a new company based in New Zealand. We Specialize in High end Luxury Residential Architecture.

Every home is bespoke and is designed to each clients individual requirements and needs.

I like to design buildings that inspire people through light and form while offering a high level of comfort and usability.

Lines of sight, proportion and balance are fundamental to the spaces I create.
Updates

August 5th is current deadline - Today's date is the 13th of August.

Target Market(s)

New Zealanders who want a custom individual home design, typically 30-65 year old males and females

Industry/Entity Type

Architecture

Contact Information for Business Card

Director - Derek Holloway
Contact Number - 0274619037
Email - info@tallowfernstudio.co.nz
Webstie - www.tallowfernstudio.co.nz
Social Media - @tallowfernstudio

Font styles to use
Sans Serif

Requirements
Must have
• Logo (Both Sides)
Website
Email
Contact Number
Social Media

Nice to have
• Texture
Should not have
• More than 3 colours - typically I would've thought 2 would be good to match the logo.

```html
<!DOCTYPE html>
<html lang="en">
<head>
<meta charset="utf-8">
<title>Tallowfern Studio – Business Cards</title>
<link rel="stylesheet" href="https://fonts.googleapis.com/css2?family=Josefin+Sans:wght@300&family=Lato:wght@700&family=Arimo:wght@400&display=swap">
<style>
  :root {
    --backdrop: #a9a9a9;
    --paper: #ffffff;
    --ink: #111111;
    --card-dark: #1b1b1b;
    --light-ink: #ffffff;
  }
  * { margin: 0; padding: 0; box-sizing: border-box; }
  html, body { width: 1065px; height: 1200px; overflow: hidden; }
  body { position: relative; background: var(--backdrop); font-family: "Arimo", Arial, sans-serif; color: var(--ink); }

  .card { position: absolute; width: 583px; height: 362px; overflow: hidden; }
  .card--front { left: 292px; top: 218px; background: var(--paper); border-radius: 0 181px 181px 0; }
  .card--back { left: 263px; top: 623px; background: var(--card-dark); border-radius: 181px 0 0 181px; color: var(--light-ink); }

  .brand-mark { position: absolute; border: 5px solid currentColor; border-radius: 50%; }
  .card--front .brand-mark { left: 78px; top: 157px; width: 46px; height: 46px; }
  .card--back .brand-mark { left: 262px; top: 114px; width: 60px; height: 60px; border-width: 6px; }

  .brand-vertical-name,
  .brand-vertical-sub {
    position: absolute; top: 61px; height: 241px;
    writing-mode: vertical-rl; transform: rotate(180deg);
    font-family: "Josefin Sans", sans-serif; font-weight: 300;
    line-height: 1; white-space: nowrap;
  }
  .brand-vertical-name { left: 152px; font-size: 21px; letter-spacing: 9.6px; }
  .brand-vertical-sub { left: 181px; font-size: 7px; letter-spacing: 35px; }

  .details { position: absolute; left: 243px; top: 80px; }
  .person-name { font-family: "Lato", sans-serif; font-weight: 700; font-size: 22px; letter-spacing: -0.3px; line-height: 1; margin-left: 2px; }
  .person-role { font-size: 16.5px; line-height: 1.2; margin-top: 1px; }
  .contact-list { list-style: none; margin-top: 22px; }
  .contact-list li { display: flex; align-items: center; gap: 6px; font-size: 17px; line-height: 21px; }
  .contact-list svg { width: 16px; height: 16px; flex: none; }
  .social-row { display: flex; gap: 4px; margin-top: 24px; }
  .social-dot { width: 23px; height: 23px; border: 1.3px solid var(--ink); border-radius: 50%; }
  .handle { font-size: 17px; margin-top: 6px; }

  .brand-stack { position: absolute; left: 0; right: 0; top: 207px; text-align: center; font-family: "Josefin Sans", sans-serif; font-weight: 300; }
  .brand-stack .brand-name { font-size: 29px; letter-spacing: 13px; margin-left: 28px; line-height: 1; }
  .brand-stack .brand-sub { font-size: 9px; letter-spacing: 49px; margin-left: 62px; margin-top: 14px; line-height: 1; }
</style>
</head>
<body>
  <section class="card card--front" aria-label="Card front">
    <div class="brand-mark" aria-hidden="true"></div>
    <span class="brand-vertical-name">TALLOWFERN</span>
    <span class="brand-vertical-sub">STUDIO</span>
    <div class="details">
      <h1 class="person-name">DEREK HOLLOWAY</h1>
      <p class="person-role">Director</p>
      <ul class="contact-list">
        <li>
          <svg viewBox="0 0 16 16" aria-hidden="true"><path d="M3.5 1.5l2.5 3-1.5 1.5c.8 2 2.5 3.7 4.5 4.5l1.5-1.5 3 2.5-1.8 2.3C6.5 13.3 2.7 9.5 1.2 4.3z" fill="#111"/><path d="M9.5 2.5a4 4 0 0 1 4 4M9.5 0.5a6 6 0 0 1 6 6" stroke="#111" stroke-width="1.3" fill="none"/></svg>
          <span>0274619037</span>
        </li>
        <li>
          <svg viewBox="0 0 16 16" aria-hidden="true"><rect x="0.5" y="3" width="15" height="10.5" fill="#111"/><path d="M0.5 3.5L8 9l7.5-5.5" stroke="#fff" stroke-width="1.2" fill="none"/></svg>
          <span>info@tallowfernstudio.co.nz</span>
        </li>
        <li>
          <svg viewBox="0 0 16 16" aria-hidden="true"><g stroke="#111" stroke-width="1.2" fill="none"><circle cx="8" cy="8" r="6.8"/><ellipse cx="8" cy="8" rx="3" ry="6.8"/><path d="M1.2 8h13.6M2.2 4.8h11.6M2.2 11.2h11.6M8 1.2v13.6"/></g></svg>
          <span>www.tallowfernstudio.co.nz</span>
        </li>
      </ul>
      <div class="social-row" aria-hidden="true">
        <span class="social-dot"></span><span class="social-dot"></span><span class="social-dot"></span>
      </div>
      <p class="handle">@tallowfernstudio</p>
    </div>
  </section>

  <section class="card card--back" aria-label="Card back">
    <div class="brand-mark" aria-hidden="true"></div>
    <div class="brand-stack">
      <p class="brand-name">TALLOWFERN</p>
      <p class="brand-sub">STUDIO</p>
    </div>
  </section>
</body>
</html>
```